Real Estate - Real Estate
Real Estate
Real Estate Company Arrange auction for land selling Real Estate services
- No scrolling - page fit to screen - You need to pick a good arabic font with good colour "If you don't know arabic keep as in photoshop". - This company have no Identity and color theme, its for you to decide - Social media links needed - Arabic interface (Right to left arrangement) - Boss photo attached need to be in the home page. - Welcome message from boss. - Section in the home page for auction announcement "lands auction". - You need to read photoshop layer name to understand the arabic name. - You decide Font colour and type the colour in the photoshop is just for showing. - No field to take any data in the home page.
kiromeltub kiromeltub
Consider it as official website
Graphics - architectural drawings
Please ignore uploaded picture
Please don't focus in Jeddah. Instead focus on "Real Estate" and add some graphics.
I uploaded some picture for jeddah please check it.
This website about jeddah - saudi arabia city only, I will upload some related photo which could be better to use, you pick what you think is better or check with google images.

```html
<!DOCTYPE html>
<html lang="ar" dir="rtl">
<head>
<meta charset="utf-8">
<title>دار الأراضي الساحلية</title>
<link rel="stylesheet" href="https://fonts.googleapis.com/css2?family=Aref+Ruqaa:wght@700&family=Amiri:wght@400;700&family=Great+Vibes&family=Open+Sans:ital,wght@0,400;0,600;1,400&display=swap">
<style>
  :root {
    --green-deep: #0d2a0d;
    --green-dark: #163d16;
    --green-mid: #2a6a22;
    --green-bright: #4fae2f;
    --green-column: #2f7a25;
    --panel: rgba(10, 30, 10, 0.72);
    --band: #0a1f0a;
    --white: #ffffff;
    --soft-white: #e8f3e4;
    --muted: #c9d8c4;
    --sky: #5c8fc4;
  }
  * { margin: 0; padding: 0; box-sizing: border-box; }
  html, body { width: 1200px; height: 665px; overflow: hidden; background: var(--green-deep); }
  .site {
    position: relative; width: 1200px; height: 665px; overflow: hidden;
    background: radial-gradient(ellipse at 55% 45%, var(--green-mid) 0%, var(--green-dark) 55%, var(--green-deep) 100%);
    font-family: "Open Sans", sans-serif; color: var(--white);
  }
  .pattern-left, .pattern-right { position: absolute; top: 0; height: 620px; }
  .pattern-left {
    left: 0; width: 300px;
    background: linear-gradient(135deg, rgba(0,0,0,0.35) 0%, rgba(40,100,30,0.25) 50%, rgba(0,0,0,0.3) 100%);
  }
  .pattern-right {
    right: 0; width: 200px;
    background: linear-gradient(225deg, rgba(0,0,0,0.3) 0%, rgba(40,100,30,0.2) 60%, rgba(0,0,0,0.25) 100%);
  }
  .brand {
    position: absolute; top: 34px; right: 72px;
    font-family: "Aref Ruqaa", serif; font-weight: 700; font-size: 92px; line-height: 1;
    color: var(--white); text-shadow: 0 0 14px rgba(200,255,190,0.55);
  }
  .leader-column {
    position: absolute; top: 168px; right: 144px; width: 228px; height: 452px;
    background: linear-gradient(180deg, var(--green-column), rgba(30,80,25,0.6));
  }
  .leader-photo {
    position: absolute; top: 180px; right: 168px; width: 180px; height: 252px;
    border: 4px solid var(--green-bright);
    background: linear-gradient(180deg, #e9ecef 0%, #cfd6d2 55%, #f4f4f4 100%);
  }
  .leader-name {
    position: absolute; top: 438px; right: 144px; width: 228px; text-align: center;
    font-family: "Amiri", serif; font-weight: 700; font-size: 19px; color: var(--soft-white);
  }
  .welcome {
    position: absolute; top: 256px; right: 384px;
    font-family: "Amiri", serif; font-weight: 400; font-size: 38px; color: var(--white);
  }
  .auction-title {
    position: absolute; top: 356px; left: 612px; direction: ltr;
    font-family: "Great Vibes", cursive; font-size: 34px; color: var(--white);
  }
  .auction-panel {
    position: absolute; top: 408px; left: 324px; width: 492px; height: 190px;
    background: var(--panel); border-radius: 10px; direction: ltr;
  }
  .auction-photo {
    position: absolute; top: 24px; left: 36px; width: 132px; height: 140px;
    background: linear-gradient(160deg, #a9cdea 0%, var(--sky) 50%, #2c4f76 100%);
  }
  .auction-text {
    position: absolute; top: 22px; left: 180px; width: 280px; text-align: right;
    font-style: italic; font-size: 14.5px; line-height: 1.38; color: var(--soft-white);
  }
  .nav-arrow {
    position: absolute; top: 86px; width: 20px; height: 20px; border-radius: 50%;
    background: var(--white); display: flex; align-items: center; justify-content: center;
  }
  .nav-arrow.prev { left: -8px; }
  .nav-arrow.next { right: -8px; }
  .follow {
    position: absolute; top: 528px; right: 144px; width: 228px; text-align: center;
    font-size: 14px; font-weight: 600; color: var(--white); direction: ltr;
  }
  .social-list {
    position: absolute; top: 560px; right: 144px; width: 228px;
    display: flex; justify-content: center; gap: 14px; direction: ltr; list-style: none;
  }
  .social-list li { display: flex; align-items: center; gap: 4px; font-size: 11px; color: var(--white); }
  .social-list .mark { width: 12px; height: 12px; background: var(--sky); }
  .footer-band {
    position: absolute; left: 0; bottom: 0; width: 1200px; height: 46px; background: var(--band);
  }
  .copyright {
    position: absolute; right: 130px; bottom: 14px; direction: ltr;
    font-size: 12px; color: var(--muted);
  }
</style>
</head>
<body>
<div class="site">
  <div class="pattern-left" role="img" aria-label="Interlaced geometric ornament in dark green"></div>
  <div class="pattern-right" role="img" aria-label="Interlaced geometric ornament in dark green"></div>

  <h1 class="brand">دار الأراضي الساحلية</h1>

  <div class="leader-column"></div>
  <div class="leader-photo" role="img" aria-label="Portrait photograph of the company chairman"></div>
  <p class="leader-name">مراد بن سامي الوادي</p>

  <h2 class="welcome">رئيس دار الأراضي الساحلية</h2>

  <h3 class="auction-title">Lands Auction</h3>
  <section class="auction-panel">
    <div class="auction-photo" role="img" aria-label="Photograph of a modern glass office tower"></div>
    <p class="auction-text">Lorem ipsum dolor sit amet, consectetur adipiscing elit. Vestibulum mattis porttitor nulla, eget eleifend metus gravida id. Nunc sollicitudin nunc at tellus pretium a pulvinar purus elementum.</p>
    <span class="nav-arrow prev"><svg width="8" height="10" viewBox="0 0 8 10"><path d="M6 1 L2 5 L6 9" fill="none" stroke="#163d16" stroke-width="2"/></svg></span>
    <span class="nav-arrow next"><svg width="8" height="10" viewBox="0 0 8 10"><path d="M2 1 L6 5 L2 9" fill="none" stroke="#163d16" stroke-width="2"/></svg></span>
  </section>

  <p class="follow">Follow Us</p>
  <ul class="social-list">
    <li><span class="mark"></span>Frendla</li>
    <li><span class="mark"></span>Linkora</li>
    <li><span class="mark"></span>Chirpa</li>
  </ul>

  <div class="footer-band"></div>
  <p class="copyright">Copyright 2014 All right reserved.</p>
</div>
</body>
</html>
```